label bath salt on glass bottle

for our bath salts (Flavours Rose, Lavender, Lemongras, mountain herbs, Mint, Cashmere) we need a label in the size of 50mm height an 55mm wide.

Target Market(s)

Prestige stores

Font styles to use
Serif
Script

Colors

Designer to choose colors to be used in the design.

Requirements
Must have
• Name of the label:
• Headline: Badesalz (can be also written in two words) Bade Salz
• Describtion of the sel: Totes Meer (comes from Dead Sea)
• Name of the different fragrances:
• Rose
• Pfingstrose (Peony)
• Lemongras
• Alpenkräuter (mountain herbs)
• Minze (mint)
• Cashmere
• Lavendel (lavender)
Nice to have
• Made with love in Switzerland
• Logos:
• Use our LOGO in the attachment or just
• FENIVU
• Switzerland

```html
<!DOCTYPE html>
<html lang="de">
<head>
<meta charset="utf-8">
<title>Badesalz – Rose Label</title>
<link rel="stylesheet" href="https://fonts.googleapis.com/css2?family=Kaushan+Script&family=PT+Serif:ital,wght@0,400;1,400&display=swap">
<style>
  :root {
    --page: #f4f4f4;
    --label-white: #ffffff;
    --frame-pink: #efa9ad;
    --rose-red: #d9282f;
    --rose-red-soft: #e0454b;
    --rule: #e7868b;
    --script-white: #ffffff;
  }
  * { margin: 0; padding: 0; box-sizing: border-box; }
  html, body {
    width: 1200px;
    height: 872px;
    overflow: hidden;
    background: var(--page);
  }
  .label {
    position: absolute;
    left: 160px;
    top: 36px;
    width: 880px;
    height: 800px;
    background: var(--label-white);
    border: 16px solid var(--frame-pink);
  }
  .label__inner {
    position: absolute;
    inset: 14px;
    background: var(--label-white);
  }
  .label__pattern-band {
    position: absolute;
    left: 0; top: 0;
    width: 100%;
    height: 360px;
    background: linear-gradient(160deg, var(--rose-red-soft), var(--rose-red) 60%);
  }
  .label__headline {
    position: absolute;
    left: 230px;
    top: 70px;
    font-family: "Kaushan Script", cursive;
    font-weight: 400;
    color: var(--script-white);
    font-size: 118px;
    line-height: 0.95;
    transform: rotate(-9deg);
    transform-origin: left top;
  }
  .label__headline span { display: block; }
  .label__headline .second { padding-left: 120px; }
  .label__badge {
    position: absolute;
    left: 50%;
    top: 360px;
    width: 120px;
    height: 120px;
    margin: -60px 0 0 -60px;
    border-radius: 50%;
    background: var(--rose-red);
    border: 4px solid var(--label-white);
  }
  .label__flavour {
    position: absolute;
    left: 0; right: 0;
    top: 446px;
    text-align: center;
    font-family: "PT Serif", serif;
    color: var(--rose-red);
  }
  .flavour__name {
    font-size: 42px;
    line-height: 1;
    letter-spacing: 1px;
  }
  .flavour__rule {
    width: 170px;
    height: 1px;
    margin: 8px auto 7px;
    background: var(--rule);
  }
  .flavour__type {
    font-size: 23px;
    letter-spacing: 6px;
  }
  .label__info {
    position: absolute;
    top: 580px;
    font-family: "PT Serif", serif;
    font-style: italic;
    font-size: 17px;
    color: var(--rose-red);
    width: 210px;
    text-align: center;
    padding-bottom: 5px;
    border-bottom: 1px solid var(--rule);
  }
  .label__info--directions { left: 150px; }
  .label__info--ingredients { left: 460px; }
</style>
</head>
<body>
  <div class="label">
    <div class="label__inner">
      <div class="label__pattern-band" role="img" aria-label="Red band with a faint scattered leaf pattern"></div>
      <h1 class="label__headline"><span>Bade</span><span class="second">Salz</span></h1>
      <div class="label__badge" role="img" aria-label="Rose flower illustration in a red circle"></div>
      <div class="label__flavour">
        <p class="flavour__name">ROSE</p>
        <div class="flavour__rule"></div>
        <p class="flavour__type">TOTES MEER</p>
      </div>
      <p class="label__info label__info--directions">Direction for use</p>
      <p class="label__info label__info--ingredients">Ingridients</p>
    </div>
  </div>
</body>
</html>
```